Einladungskarten-Design für jährliches Sommerfest
Zielgruppe
Wir sind die Kreisverwaltung des Landkreises Velsbrück-Auental (das Landratsamt) und möchten unsere Mitarbeiter zum jährlichen Sommerfest einladen. Jedes Jahr stehen diese Feste unter einem anderen Motto- das diesjährige lautet: Karibik.
Aufgabenstellung
Wegen des karibischen Mottos möchten wir die Einladung in Form einer Postkarte designen lassen (vorne Bild, hinten Text). Das Design soll uns als druckfähige Datei in einem gängigen Postkarten-Format zugehen, das sich über Papierwerk-Blitz oder Satz-und-Bogen-Shop produzieren lässt. Bitte integrieren Sie wenn möglich keine kostenpflichtigen Bilder oder Schriftarten. Der Text lautet:
Liebe Kolleginnen und Kollegen,
Hannelore Wibbeking, Gudrun Ostertag und ich senden Euch Urlaubsgrüße aus der Karibik!
Hier ist es so schön, dass wir Euch direkt einladen möchten – zu einer „Goldenen Brise“ am Donnerstag, 16. August ab 17 Uhr.
Wir feiern natürlich am Strand (Amtshof Velsbrück, direkt am See). Dresscode: sommerlich, blumig, legere!
Bei einem kühlen Getränk oder fruchtigem Cocktail an der Bar wollen wir mit euch ins Gespräch kommen und einen gemütlichen Sommerabend verbringen.
Dieser Kurzurlaub ist bereits vom Fachbereich Personal genehmigt und kostet Euch lediglich fünf Euro pro Person. In unserer vier Sterne Club-Anlage sind Abendessen vom Buffet, alkoholfreie Getränke und zwei Stunden Zeitgutschrift inklusive.
Eure Reiseunterlagen könnt Ihr über das Personal-Info-System bis Mittwoch, 8. August reservieren.
Sommerliche Grüße
Landrat Bernd Ulrich Tomaschek

```html
<!DOCTYPE html>
<html lang="de">
<head>
<meta charset="utf-8">
<title>Einladung Sommerfest – Urlaubsgrüße aus der Karibik</title>
<link rel="stylesheet" href="https://fonts.googleapis.com/css2?family=Rubik:wght@800&family=PT+Sans+Narrow:wght@400;700&family=Caveat:wght@600&display=swap">
<style>
  :root {
    --page: #ece7e1;
    --sky-top: #3b2a78;
    --sky-violet: #8a4fb5;
    --sky-pink: #d76a9a;
    --sky-orange: #f08a3c;
    --sky-yellow: #f8d23a;
    --white: #ffffff;
    --ink: #1c1a24;
    --script-blue: #1565b0;
    --card-pink: #f1d9ea;
    --card-cream: #fdf6ea;
    --rule: #5a6275;
    --palm-tint: #c9b9d8;
  }
  * { box-sizing: border-box; margin: 0; padding: 0; }
  html, body { width: 1200px; height: 848px; overflow: hidden; background: var(--page); }
  .stage { position: relative; width: 1200px; height: 848px; }

  /* Front */
  .card-front {
    position: absolute; left: 48px; top: 124px; width: 424px; height: 600px;
    overflow: hidden; box-shadow: 0 6px 18px rgba(0,0,0,.18);
  }
  .front-scene {
    position: absolute; inset: 0;
    background: linear-gradient(180deg, var(--sky-top) 0%, var(--sky-violet) 28%, var(--sky-pink) 58%, var(--sky-orange) 82%, var(--sky-yellow) 100%);
  }
  .title-frame {
    position: absolute; left: 64px; top: 168px; width: 332px; height: 312px;
    border: 5px solid var(--white);
    display: flex; align-items: center; justify-content: center;
  }
  .title {
    font-family: "Rubik", sans-serif; font-weight: 800; color: var(--white);
    font-size: 60px; line-height: 0.98; letter-spacing: 3px; text-align: left;
    text-shadow: 3px 4px 6px rgba(40,20,60,.45);
  }

  /* Back */
  .card-back {
    position: absolute; left: 540px; top: 212px; width: 612px; height: 424px;
    overflow: hidden; box-shadow: 0 6px 18px rgba(0,0,0,.18);
    background: linear-gradient(160deg, var(--card-pink) 0%, #f6e6f0 45%, var(--card-cream) 100%);
  }
  .palm-column {
    position: absolute; left: 298px; top: 14px; width: 84px; height: 410px;
    background: linear-gradient(180deg, rgba(60,40,90,.18), rgba(60,40,90,.08));
  }
  .palm-faint {
    position: absolute; right: 0; top: 20px; width: 160px; height: 330px;
    background: linear-gradient(180deg, rgba(201,185,216,.25), rgba(201,185,216,0));
  }
  .letter { position: absolute; left: 24px; top: 22px; width: 300px; }
  .greeting, .signature, .address-line {
    font-family: "Caveat", cursive; font-weight: 600; color: var(--script-blue);
  }
  .greeting { font-size: 25px; line-height: 1; margin-bottom: 8px; }
  .body {
    font-family: "PT Sans Narrow", sans-serif; font-size: 11.6px; line-height: 15.4px; color: var(--ink);
  }
  .body p { margin-bottom: 14px; }
  .body strong { font-weight: 700; }
  .body .closing { margin-bottom: 2px; }
  .signature { font-size: 22px; line-height: 1.1; }

  .stamp-box {
    position: absolute; left: 506px; top: 24px; width: 72px; height: 86px;
    border: 1.4px solid var(--rule);
  }
  .address { position: absolute; left: 368px; top: 198px; width: 212px; }
  .address-line {
    font-size: 23px; line-height: 1; height: 38px; padding-top: 6px;
    border-bottom: 1px solid var(--rule); white-space: nowrap;
  }
</style>
</head>
<body>
<main class="stage">
  <section class="card-front">
    <div class="front-scene" role="img" aria-label="Silhouetten von Palmen vor einem Sonnenuntergangshimmel in Violett, Pink, Orange und Gelb"></div>
    <div class="title-frame">
      <h1 class="title">URLAUBS<br>GRÜSSE<br>AUS DER<br>KARIBIK</h1>
    </div>
  </section>

  <section class="card-back">
    <div class="palm-faint" role="img" aria-label="Blasse Palmensilhouette im Hintergrund"></div>
    <div class="palm-column" role="img" aria-label="Dunkle Palmensilhouetten"></div>

    <article class="letter">
      <p class="greeting">Liebe Kolleginnen und Kollegen,</p>
      <div class="body">
        <p>Hannelore Wibbeking, Gudrun Ostertag und ich senden Euch<br>Urlaubsgrüße aus der Karibik!</p>
        <p>Hier ist es so schön, dass wir Euch direkt einladen möchten –<br>zu einer „Goldenen Brise“ am <strong>Donnerstag, 16. August ab 17 Uhr.</strong></p>
        <p>Wir feiern natürlich am Strand (Amtshof Velsbrück, direkt am See).<br>Dresscode: sommerlich, blumig, legere!<br>Bei einem kühlen Getränk oder fruchtigem Cocktail an der Bar<br>wollen wir mit euch ins Gespräch kommen und einen gemütlichen<br>Sommerabend verbringen.</p>
        <p>Dieser Kurzurlaub ist bereits vom Fachbereich Personal genehmigt<br>und kostet Euch lediglich fünf Euro pro Person. In unserer vier<br>Sterne Club-Anlage sind Abendessen vom Buffet, alkoholfreie<br>Getränke und zwei Stunden Zeitgutschrift inklusive.</p>
        <p>Eure Reiseunterlagen könnt Ihr über das Personal-<br>Info-System bis Mittwoch, 8. August reservieren.</p>
        <p class="closing">Sommerliche Grüße</p>
      </div>
      <p class="signature">Landrat Bernd Ulrich Tomaschek</p>
    </article>

    <div class="stamp-box"></div>

    <address class="address">
      <div class="address-line">An die</div>
      <div class="address-line">Kolleginnen und Kollegen</div>
      <div class="address-line">der Kreisverwaltung des</div>
      <div class="address-line">LK Velsbrück-Auental</div>
    </address>
  </section>
</main>
</body>
</html>
```